Flyer-Design für Ankauf gebrauchter Bücher
Zielgruppe
Alle die Ihre gebrauchen Bücher verkaufen möchten.
Aufgabenstellung
Modern, farblich an alten Flyer und Logo anpassen
Achtung neue Adresse und Telefon Nr.
Buchhandel Markus Ehrlein
Alwin Tressel Straße 9
D-65417 Wendelsau
Tel.: 06471/5829316

```html
<!DOCTYPE html>
<html lang="de">
<head>
<meta charset="utf-8">
<title>Buchhandel Markus Ehrlein – Ankauf gebrauchter Bücher</title>
<link rel="stylesheet" href="https://fonts.googleapis.com/css2?family=Cabin:wght@400;500&family=Roboto:ital,wght@0,400;1,900&display=swap">
<style>
  :root {
    --magenta: #e2047f;
    --white: #ffffff;
    --ink: #1d1d1b;
    --mint: #9cc4a4;
    --mint-deep: #6fae95;
  }
  * { margin: 0; padding: 0; box-sizing: border-box; }
  html, body { width: 1200px; height: 855px; overflow: hidden; background: var(--white); }
  .flyer {
    position: relative;
    width: 1200px;
    height: 855px;
    overflow: hidden;
    font-family: "Cabin", sans-serif;
  }
  .backdrop-photo {
    position: absolute; inset: 0;
    background:
      radial-gradient(circle at 62% 30%, rgba(255,236,180,.75), transparent 40%),
      radial-gradient(circle at 95% 20%, rgba(255,230,160,.6), transparent 30%),
      linear-gradient(120deg, #b9d3b0 0%, var(--mint) 45%, var(--mint-deep) 100%);
  }
  .books-photo {
    position: absolute;
    left: 634px; top: 95px; width: 420px; height: 570px;
    border-radius: 6px;
    background: linear-gradient(180deg, #f1e2c4 0%, #e9cf9e 40%, #c79d62 70%, #e7cc98 100%);
    opacity: .92;
  }
  .shapes { position: absolute; inset: 0; }
  .brand {
    position: absolute; left: 30px; top: 56px;
    display: flex; align-items: center; gap: 18px;
  }
  .brand-square { width: 70px; height: 70px; background: var(--magenta); flex: none; }
  .brand-name {
    font-family: "Cabin", sans-serif;
    font-weight: 400; font-size: 32px; letter-spacing: 2px; line-height: 35px;
    color: var(--ink); text-transform: uppercase;
  }
  .headline {
    position: absolute; left: 40px; top: 262px;
    font-family: "Roboto", sans-serif; font-style: italic; font-weight: 900;
    color: var(--magenta);
  }
  .headline-main { font-size: 62px; letter-spacing: 5.5px; line-height: 1; }
  .headline-sub { display: block; font-size: 47px; letter-spacing: 3px; line-height: 44px; margin-top: 4px; }
  .genres {
    position: absolute; left: 39px; top: 440px; width: 303px; height: 232px;
    background: var(--magenta); color: var(--white);
    padding: 16px 0 0 19px;
    font-family: "Roboto", sans-serif; font-size: 20.5px; letter-spacing: 1px; line-height: 24.5px;
    list-style: none;
  }
  .cta {
    position: absolute; right: 44px; top: 638px; text-align: right;
    color: var(--white); font-size: 30px; line-height: 30px;
  }
  .phone {
    position: absolute; right: 50px; top: 708px;
    font-family: "Roboto", sans-serif; font-style: italic; font-weight: 900;
    font-size: 64px; letter-spacing: 4px; color: var(--white); line-height: 1;
  }
  .visit {
    position: absolute; right: 46px; top: 781px;
    font-size: 20px; color: var(--white); letter-spacing: .3px;
  }
  .address, .hours {
    position: absolute; top: 810px; font-size: 19px; color: var(--ink); letter-spacing: .5px;
  }
  .address { left: 134px; }
  .hours { right: 50px; }
</style>
</head>
<body>
<main class="flyer">
  <div class="backdrop-photo" role="img" aria-label="Foto: goldene Lichtpunkte (Bokeh) auf mintgrünem Hintergrund"></div>
  <div class="books-photo" role="img" aria-label="Foto: hoher Stapel alter, gebrauchter Bücher"></div>

  <svg class="shapes" width="1200" height="855" viewBox="0 0 1200 855" aria-hidden="true">
    <path d="M0 0 H1200 V8 C900 70 560 150 0 218 Z" fill="rgba(255,255,255,.9)"/>
    <path d="M0 806 C300 740 620 668 1200 590 V855 H0 Z" fill="var(--magenta)"/>
  </svg>

  <header class="brand">
    <span class="brand-square"></span>
    <span class="brand-name">Buchhandel<br>Markus Ehrlein</span>
  </header>

  <h1 class="headline">
    <span class="headline-main">AUSGELESEN?</span>
    <span class="headline-sub">Wir kaufen Ihre<br>gebrauchten!</span>
  </h1>

  <ul class="genres">
    <li>Kinder-, Kochbücher</li>
    <li>Fach- und Sachbücher</li>
    <li>Biografien/Politik</li>
    <li>Taschenbücher</li>
    <li>Bildbände, Technik</li>
    <li>historische und</li>
    <li>antiquarische Bücher</li>
    <li>und viele weitere Themen.</li>
  </ul>

  <p class="cta">Vereinbaren Sie gleich<br>einen Termin mit uns!</p>
  <p class="phone">06471/5829316</p>
  <p class="visit">Wir kommen gerne zu Ihnen und unterbreiten Ihnen ein Angebot (auch für große Buch-Auflösungen).</p>
  <p class="address">Buchhandel Markus Ehrlein, Alwin Tressel Straße 9, D-65417 Wendelsau</p>
  <p class="hours">Öffnungszeiten: Mo.-Fr. von 9-16 Uhr</p>
</main>
</body>
</html>
```